Quiet Lanterns: Reflections on Tide Charts and Orchard Rituals Among Coastal Villages.

Book cover, spine, and back cover. This is written by Dr. T. HALVERSEN, and will be an educational book for academics, government officials, and the general population.
I'm imagining the outline of a person with am active mind in the middle. It would be overlayed on top of a circular galaxy on the background. On either side, smaller, perhaps in the background would be a cross on one side and a few uaps (ufo) of different shapes on the other (orb, saucer, triangle. ) beneath allnof this would be something symbolizing society - either the earth itself or the skyline of a large city.
By Dr. T. HALVERSEN along the bottom, i presume. (Ai cannot make this, but I've included a few examples nonetheless. )
I assume I will be given the opportunity to write a synopsis on the back cover. I will be self publishing and selling from my website.
Target Market(s)
Academics, professionals, church leaders, government officials, and the general public.
Industry/Entity Type
Professional and community education
Requirements
Must have
- It should look like a ph.d level book. Eye catching but not overly fantastical. (Its an educational book not a comic book)
Should not have
- Not hollywood or fantasy book looking. It should look a graduate school book. The tone is quite serious.

```html
<!DOCTYPE html>
<html lang="en">
<head>
<meta charset="utf-8">
<title>Quiet Lanterns — Book Jacket</title>
<link href="https://fonts.googleapis.com/css2?family=Marcellus&family=Marcellus+SC&family=Tinos&display=swap" rel="stylesheet">
<style>
  :root {
    --page-bg: #f4f3f5;
    --cover-top: #3d3448;
    --cover-mid: #2f2438;
    --cover-bottom: #2a1526;
    --ink-light: #ffffff;
    --ink-soft: #eae6ee;
    --accent-cyan: #5fd3de;
    --art-blue: #2f6f9a;
    --art-violet: #6a3f8f;
    --art-magenta: #b0467f;
    --art-deep: #1c2a44;
  }
  * { box-sizing: border-box; margin: 0; padding: 0; }
  html, body {
    width: 1200px; height: 800px; overflow: hidden;
    background: var(--page-bg);
  }
  .jacket {
    position: absolute; left: 178px; top: 100px;
    display: flex; height: 600px;
  }
  .back-cover, .spine, .front-cover {
    height: 100%;
    background: linear-gradient(160deg, var(--cover-top) 0%, var(--cover-mid) 50%, var(--cover-bottom) 100%);
    color: var(--ink-light);
    position: relative;
  }
  .back-cover { width: 400px; padding: 48px 44px 0; }
  .spine {
    width: 44px;
    background: linear-gradient(90deg, var(--cover-bottom), var(--cover-mid) 50%, var(--cover-bottom));
    display: flex; align-items: center; justify-content: center;
  }
  .front-cover { width: 400px; }

  .back-title {
    font-family: "Marcellus", serif;
    font-size: 38px; line-height: 0.95; text-align: center;
    letter-spacing: 0.5px;
  }
  .synopsis {
    font-family: "Tinos", serif;
    font-size: 10.2px; line-height: 1.22; color: var(--ink-soft);
    text-align: justify; margin-top: 16px;
  }
  .synopsis + .synopsis { margin-top: 0; }
  .back-emblem { display: block; margin: 22px auto 0; }
  .synopsis-lower { margin-top: 22px; }

  .spine-text {
    writing-mode: vertical-rl;
    font-family: "Marcellus", serif;
    font-size: 22px; letter-spacing: 1px; white-space: nowrap;
    display: flex; gap: 44px;
  }

  .front-title {
    font-family: "Marcellus", serif;
    font-size: 64px; line-height: 0.92; text-align: center;
    margin-top: 28px; letter-spacing: 0.5px;
  }
  .front-subtitle {
    font-family: "Marcellus SC", serif;
    font-size: 14.5px; line-height: 1.3; text-align: center;
    color: var(--ink-soft); margin: 16px 26px 0;
  }
  .cover-art {
    position: absolute; left: 0; right: 0; top: 232px; height: 290px;
    background:
      radial-gradient(circle at 50% 45%, rgba(255,255,255,0.55) 0%, rgba(150,120,220,0.5) 10%, transparent 26%),
      radial-gradient(circle at 50% 48%, var(--art-violet) 0%, var(--art-magenta) 32%, var(--art-blue) 44%, transparent 58%),
      linear-gradient(180deg, var(--cover-mid) 0%, var(--art-deep) 60%, var(--cover-bottom) 100%);
  }
  .front-author {
    position: absolute; left: 0; right: 0; bottom: 26px;
    font-family: "Marcellus", serif;
    font-size: 34px; text-align: center; letter-spacing: 0.5px;
  }
</style>
</head>
<body>
  <main class="jacket">
    <section class="back-cover">
      <h2 class="back-title">QUIET<br>LANTERNS</h2>
      <p class="synopsis">Lorem ipsum dolor sit amet, consectetuer adipiscing elit, sed diam nonummy nibh euismod tincidunt ut laoreet dolore magna aliquam erat volutpat. Ut wisi enim ad minim veniam, quis nostrud exerci tation ullamcorper suscipit lobortis nisl ut aliquip ex ea commodo consequat. Duis autem vel eum iriure dolor in hendrerit in vulputate velit esse molestie consequat, vel illum dolore eu feugiat nulla facilisis at vero eros et accumsan et iusto odio dignissim qui blandit praesent luptatum zzril delenit augue duis dolore te feugait nulla facilisi.</p>
      <p class="synopsis">Lorem ipsum dolor sit amet, cons ectetuer adipiscing elit, sed diam nonummy nibh euismod tincidunt ut laoreet dolore magna aliquam erat volutpat. Ut wisi enim ad minim veniam, quis nostrud exerci tation ullamcorper suscipit lobortis</p>
      <svg class="back-emblem" width="90" height="108" viewBox="0 0 90 108" aria-hidden="true">
        <ellipse cx="45" cy="54" rx="43" ry="52" fill="none" stroke="var(--accent-cyan)" stroke-width="1.2"/>
      </svg>
      <p class="synopsis synopsis-lower">Lorem ipsum dolor sit amet, consectetuer adipiscing elit, sed diam nonummy nibh euismod tincidunt ut laoreet dolore magna aliquam erat volutpat. Ut wisi enim ad minim veniam, quis nostrud exerci tation ullamcorper suscipit lobortis nisl ut aliquip ex ea commodo consequat. Duis autem vel eum iriure dolor in hendrerit in vulputate velit esse molestie consequat, vel illum dolore eu feugiat nulla facilisis at vero eros et accumsan et iusto odio dignissim qui blandit praesent luptatum zzril delenit augue duis dolore te feugait nulla facilisi. Lorem ipsum dolor sit amet, cons ectetuer adipiscing elit, sed diam nonummy nibh euismod tincidunt ut laoreet dolore magna aliquam erat volutpat. Ut wisi enim ad minim veniam, quis nostrud exerci tation ullamcorper suscipit lobortis</p>
    </section>

    <section class="spine">
      <div class="spine-text">
        <span class="spine-title">QUIET LANTERNS</span>
        <span class="spine-author">DR. T. HALVERSEN</span>
      </div>
    </section>

    <section class="front-cover">
      <h1 class="front-title">QUIET<br>LANTERNS</h1>
      <p class="front-subtitle">Reflections on Tide Charts and Orchard Rituals Among Coastal Villages</p>
      <div class="cover-art" role="img" aria-label="Illustration: silhouette of a head with a glowing brain set against a circular galaxy, a lone figure standing at its base, hovering craft casting light beams on either side, a cross and a triangle symbol at the edges, and a city skyline with a church spire along the bottom"></div>
      <p class="front-author">DR. T. HALVERSEN</p>
    </section>
  </main>
</body>
</html>
```